STATIONERY and Brand ID for VelmiBank

We need a family of identical Brand guide
Call Card
Envelope
Letterhead
Poster
Brochure

It needs to have an international Fee/

The ARCHITECTURE/STRUCTURE must show the highest level of creativity

1. Call card could be two sided
2. cal card can have a a flap
3. Call card can have a curved edge

Target Market(s)

Business and bank clients

Industry/Entity Type

Bank

Requirements
Must have
• the logo atatched
• the colour scheme must be used
• There must be a common look and feel and they must have the same DNA

```html
<!DOCTYPE html>
<html lang="en">
<head>
<meta charset="utf-8">
<title>VelmiBank – Business Card</title>
<link rel="stylesheet" href="https://fonts.googleapis.com/css2?family=Arimo:wght@400;700&display=swap">
<style>
  :root {
    --navy: #22336f;
    --green: #77c043;
    --white: #ffffff;
    --backdrop: #e4e5e7;
    --card-radius: 22px;
  }
  * { margin: 0; padding: 0; box-sizing: border-box; }
  html, body { width: 1200px; height: 800px; overflow: hidden; }
  body {
    background: var(--backdrop);
    font-family: "Arimo", Arial, sans-serif;
    position: relative;
  }
  .card {
    position: absolute;
    width: 500px;
    height: 290px;
    border-radius: var(--card-radius);
    overflow: hidden;
    box-shadow: 0 10px 26px rgba(0,0,0,0.16);
  }

  /* ---------- Shared wordmark ---------- */
  .wordmark {
    position: absolute;
    font-weight: 700;
    font-size: 50px;
    letter-spacing: -1.5px;
    line-height: 1;
    white-space: nowrap;
  }

  /* ---------- Back of card ---------- */
  .card--back {
    left: 70px; top: 255px;
    background: var(--navy);
  }
  .card--back .inset-frame {
    position: absolute; inset: 13px;
    border: 3px solid var(--white);
    border-radius: 14px;
  }
  .card--back .wordmark {
    left: 0; right: 0; top: 120px;
    text-align: center;
    color: var(--white);
  }

  /* ---------- Front of card ---------- */
  .card--front {
    left: 630px; top: 255px;
    background: var(--white);
  }
  .card--front .wave { position: absolute; inset: 0; }
  .card--front .wordmark {
    left: 60px; top: 56px;
    color: var(--navy);
  }

  .holder {
    position: absolute;
    right: 272px; top: 188px;
    text-align: right;
  }
  .holder__name {
    color: var(--green);
    font-weight: 700;
    font-size: 17px;
    line-height: 1.2;
  }
  .holder__title {
    color: var(--white);
    font-size: 14px;
    line-height: 1.3;
  }
  .contact-divider {
    position: absolute;
    left: 246px; top: 160px;
    width: 2px; height: 90px;
    background: var(--white);
  }
  .contact-list {
    position: absolute;
    left: 258px; top: 150px;
    list-style: none;
    color: var(--white);
    font-size: 13.5px;
    line-height: 17px;
  }
  .contact-list li { display: flex; align-items: center; gap: 6px; }
  .contact-list .address { display: block; margin-bottom: 1px; }
  .contact-icon { width: 12px; height: 12px; flex: none; }
</style>
</head>
<body>

  <section class="card card--back" aria-label="Business card, back">
    <div class="inset-frame"></div>
    <p class="wordmark">VelmiBank</p>
  </section>

  <section class="card card--front" aria-label="Business card, front">
    <svg class="wave" viewBox="0 0 500 290" preserveAspectRatio="none" aria-hidden="true">
      <path d="M0,156 C160,146 350,116 500,40 L500,290 L0,290 Z" fill="var(--navy)"/>
      <path d="M40,150 C210,134 380,100 500,20 L500,36 C380,110 210,142 40,150 Z" fill="var(--green)"/>
    </svg>

    <p class="wordmark">VelmiBank</p>

    <div class="holder">
      <p class="holder__name">Your Name</p>
      <p class="holder__title">President</p>
    </div>

    <div class="contact-divider"></div>

    <ul class="contact-list">
      <li class="address">1234 , your street City,<br>ST, 12345</li>
      <li>
        <svg class="contact-icon" viewBox="0 0 24 24" aria-hidden="true"><path fill="var(--green)" d="M6.6 10.8a15.1 15.1 0 0 0 6.6 6.6l2.2-2.2c.3-.3.7-.4 1-.2 1.1.4 2.3.6 3.6.6.6 0 1 .4 1 1V20c0 .6-.4 1-1 1A17 17 0 0 1 3 4c0-.6.4-1 1-1h3.5c.6 0 1 .4 1 1 0 1.3.2 2.5.6 3.6.1.3 0 .7-.2 1z"/></svg>
        (0000) 123-4567
      </li>
      <li>
        <svg class="contact-icon" viewBox="0 0 24 24" aria-hidden="true"><path fill="var(--green)" d="M2 5h20v14H2z"/><path d="M2 5l10 8 10-8" fill="none" stroke="var(--navy)" stroke-width="2"/></svg>
        hello@velmibank.co.uk
      </li>
      <li>
        <svg class="contact-icon" viewBox="0 0 24 24" aria-hidden="true"><circle cx="12" cy="12" r="10" fill="var(--green)"/><path d="M2 12h20M12 2c3 3 3 17 0 20M12 2c-3 3-3 17 0 20" fill="none" stroke="var(--navy)" stroke-width="1.5"/></svg>
        www.velmibank.co.uk
      </li>
    </ul>
  </section>

</body>
</html>
```